Business cards for the RL Group

We are looking for a template for our new business cards for our company that we can edit ourselves.
You will find our company colors in the logo. the logo on the back and on the front
first name Last Name
position
E-mail address
mobile number
landline number
Companies we have 2 RL Sicherheit GmbH and RL Services GmbH
address
Lindenbergweg 42
22459 Hamburg
www.rlgruppe-nord.de

Something modern, simple but professional

if you have any questions, bring it on.

Sicherheit

Steht in der Beschreibung

F0912C
F2A743
F7CA91
FBE8D2
FDF5EE

• recognition value
• professional
• Playful

```html
<!DOCTYPE html>
<html lang="de">
<head>
<meta charset="utf-8">
<title>RL Gruppe – Visitenkarten</title>
<link href="https://fonts.googleapis.com/css2?family=Montserrat:wght@400;700&display=swap" rel="stylesheet">
<style>
  :root {
    --backdrop: #8e8e8e;
    --card-white: #ffffff;
    --card-dark: #565656;
    --ink: #505050;
    --text: #3a3a3a;
    --accent: #f28a1a;
    --on-dark: #ffffff;
  }
  * { margin: 0; padding: 0; box-sizing: border-box; }
  html, body {
    width: 1200px; height: 1056px; overflow: hidden;
    background: var(--backdrop);
    font-family: "Montserrat", sans-serif;
  }
  .stage {
    position: relative; width: 1200px; height: 1056px;
  }
  .card {
    position: absolute; left: 320px;
    width: 560px; height: 320px;
    box-shadow: 0 10px 24px rgba(0,0,0,0.25);
  }
  .card--front { top: 178px; background: var(--card-white); }
  .card--back { top: 558px; background: var(--card-dark); }

  .brand {
    position: absolute; display: flex; align-items: center; gap: 14px;
  }
  .brand__dot {
    width: 34px; height: 34px; border-radius: 50%;
    background: var(--accent); flex: none;
  }
  .brand__name {
    font-weight: 700; font-size: 40px; letter-spacing: 1px; line-height: 1;
  }
  .card--front .brand { left: 36px; top: 138px; }
  .card--front .brand__name { color: var(--ink); }
  .card--back .brand { left: 50%; top: 50%; transform: translate(-50%, -50%); }
  .card--back .brand__name { color: var(--on-dark); font-size: 46px; }

  .person { position: absolute; right: 36px; top: 44px; text-align: right; }
  .person__name {
    color: var(--accent); font-weight: 700; font-size: 30px;
    letter-spacing: 1px; text-transform: uppercase; line-height: 1.05;
  }
  .person__role { color: var(--text); font-size: 19px; margin-top: 2px; }

  .contact {
    position: absolute; left: 330px; top: 170px;
    color: var(--text); font-size: 11.5px; line-height: 1.45;
  }
  .contact__address { margin-bottom: 10px; }
  .contact__list { list-style: none; }
  .contact__item { display: flex; align-items: center; gap: 7px; }
  .contact__icon { width: 10px; height: 10px; fill: var(--accent); flex: none; }
  .contact__item--plain { padding-left: 17px; }
</style>
</head>
<body>
<main class="stage">
  <section class="card card--front" aria-label="Vorderseite">
    <div class="brand">
      <span class="brand__dot"></span>
      <span class="brand__name">RL Gruppe</span>
    </div>
    <div class="person">
      <p class="person__name">Lena Marquardt</p>
      <p class="person__role">Director / CEO</p>
    </div>
    <div class="contact">
      <p class="contact__address">Lindenbergweg 42<br>22459 Hamburg</p>
      <ul class="contact__list">
        <li class="contact__item">
          <svg class="contact__icon" viewBox="0 0 10 10"><rect x="2.5" y="0.5" width="5" height="9" rx="1"/></svg>
          (0)176-555218 40
        </li>
        <li class="contact__item">
          <svg class="contact__icon" viewBox="0 0 10 10"><path d="M2 0.5 L4 2.5 L3 4 Q4.5 6 6 7 L7.5 6 L9.5 8 L8 9.5 Q3 9 0.5 2 Z"/></svg>
          040 555319
        </li>
        <li class="contact__item">
          <svg class="contact__icon" viewBox="0 0 10 10"><path d="M0.5 2 H9.5 V8.5 H0.5 Z M1 2.5 L5 5.5 L9 2.5" stroke="#fff" stroke-width="0.8"/></svg>
          info@rlgruppe-nord.com
        </li>
        <li class="contact__item">
          <svg class="contact__icon" viewBox="0 0 10 10"><path d="M5 0.5 L9 5 H6.3 V9.5 H3.7 V5 H1 Z"/></svg>
          www.rlgruppe-nord.com
        </li>
        <li class="contact__item contact__item--plain">www.rlgruppe-nord.de</li>
      </ul>
    </div>
  </section>

  <section class="card card--back" aria-label="Rückseite">
    <div class="brand">
      <span class="brand__dot"></span>
      <span class="brand__name">RL Gruppe</span>
    </div>
  </section>
</main>
</body>
</html>
```